Life Coach for Lawyers Business Card Design

Elegant, original, business card design for life coaching service for associate attorneys who work in big law and struggle with stress, overwhelm, and time management. Double sided design.

Target Market(s)

Women associate attorneys who work in big law and struggle with stress, overwhelm, and time management.

Industry/Entity Type

Life Coaching

Contact Information for Business Card

Marissa Pendrell
Life Coach
518.677.3941
calmbriefcounsel.net
marissa@calmbriefcounsel.net
@calmbriefcounsel (Instagram)

Font styles to use
Other font styles liked:
• Silver South font duo. See uploaded files.

Requirements
Must have
• Icons for phone, website, email, and Instagram instead of words. Specific colors used in my logo (171B2B, 421121, FFFFFF)
Nice to have
• Foil. Embossed. Feminine design.
Should not have
• Any colors other than those used in logo. See uploaded files.

```html
<!DOCTYPE html>
<html lang="en">
<head>
<meta charset="utf-8">
<title>Calm Brief Counsel — Business Card</title>
<link rel="stylesheet" href="https://fonts.googleapis.com/css2?family=Tinos:wght@400;700&display=swap">
<style>
  :root {
    --ink: #171B2B;
    --wine: #421121;
    --paper: #FFFFFF;
    --backdrop: #ECECEC;
    --card-w: 900px;
    --card-h: 514px;
  }
  * { box-sizing: border-box; margin: 0; padding: 0; }
  html, body {
    width: 1200px;
    height: 1200px;
    overflow: hidden;
    background: var(--backdrop);
  }
  .sheet {
    width: 1200px;
    height: 1200px;
    display: flex;
    flex-direction: column;
    align-items: center;
    justify-content: center;
    gap: 56px;
  }
  .card {
    position: relative;
    width: var(--card-w);
    height: var(--card-h);
    box-shadow: 0 6px 18px rgba(23, 27, 43, 0.12);
    font-family: "Tinos", "Times New Roman", serif;
  }

  /* Back side */
  .card--back {
    background: var(--wine);
    display: flex;
    align-items: center;
    justify-content: center;
  }
  .seal {
    width: 270px;
    height: 270px;
    border: 2px solid var(--paper);
    border-radius: 50%;
    display: flex;
    align-items: center;
    justify-content: center;
  }
  .seal__name {
    color: var(--paper);
    font-size: 22px;
    font-weight: 400;
    letter-spacing: 0.08em;
    text-transform: uppercase;
    text-align: center;
    line-height: 1.5;
    width: 200px;
  }

  /* Front side */
  .card--front { background: var(--paper); color: var(--ink); }
  .brand-name {
    position: absolute;
    left: 72px;
    top: 110px;
    color: var(--wine);
    font-size: 34px;
    font-weight: 400;
    letter-spacing: 0.06em;
    text-transform: uppercase;
  }
  .identity {
    position: absolute;
    left: 72px;
    top: 302px;
  }
  .identity__name {
    font-size: 40px;
    font-weight: 700;
    line-height: 1.1;
  }
  .identity__role {
    font-size: 25px;
    margin-top: 4px;
  }
  .divider {
    position: absolute;
    left: 413px;
    top: 296px;
    width: 3px;
    height: 118px;
    background: var(--wine);
  }
  .contacts {
    position: absolute;
    left: 436px;
    top: 294px;
    list-style: none;
  }
  .contacts__item {
    display: flex;
    align-items: center;
    gap: 12px;
    font-size: 25px;
    line-height: 30px;
  }
  .contacts__icon {
    width: 20px;
    height: 20px;
    flex: none;
  }
</style>
</head>
<body>
<main class="sheet">

  <section class="card card--back" aria-label="Card back">
    <div class="seal">
      <p class="seal__name">Calm Brief Counsel</p>
    </div>
  </section>

  <section class="card card--front" aria-label="Card front">
    <h1 class="brand-name">Calm Brief Counsel</h1>

    <div class="identity">
      <p class="identity__name">Marissa Pendrell</p>
      <p class="identity__role">Life Coach</p>
    </div>

    <div class="divider"></div>

    <ul class="contacts">
      <li class="contacts__item">
        <svg class="contacts__icon" viewBox="0 0 24 24" aria-hidden="true">
          <path fill="#171B2B" d="M6.6 10.8a15.2 15.2 0 0 0 6.6 6.6l2.2-2.2a1 1 0 0 1 1-.25 11.4 11.4 0 0 0 3.6.57 1 1 0 0 1 1 1V20a1 1 0 0 1-1 1A17 17 0 0 1 3 4a1 1 0 0 1 1-1h3.5a1 1 0 0 1 1 1c0 1.25.2 2.45.57 3.57a1 1 0 0 1-.25 1z"/>
        </svg>
        <span>518.677.3941</span>
      </li>
      <li class="contacts__item">
        <svg class="contacts__icon" viewBox="0 0 24 24" aria-hidden="true">
          <g fill="none" stroke="#171B2B" stroke-width="2">
            <circle cx="12" cy="12" r="9.5"/>
            <ellipse cx="12" cy="12" rx="4" ry="9.5"/>
            <path d="M2.5 12h19M4 7h16M4 17h16"/>
          </g>
        </svg>
        <span>calmbriefcounsel.net</span>
      </li>
      <li class="contacts__item">
        <svg class="contacts__icon" viewBox="0 0 24 24" aria-hidden="true">
          <g fill="none" stroke="#171B2B" stroke-width="2" stroke-linejoin="round">
            <rect x="2.5" y="5" width="19" height="14" rx="1.5"/>
            <path d="M3 6l9 7 9-7"/>
          </g>
        </svg>
        <span>marissa@calmbriefcounsel.net</span>
      </li>
      <li class="contacts__item">
        <svg class="contacts__icon" viewBox="0 0 24 24" aria-hidden="true">
          <rect x="3" y="3" width="18" height="18" rx="4" fill="none" stroke="#171B2B" stroke-width="2"/>
        </svg>
        <span>@calmbriefcounsel</span>
      </li>
    </ul>
  </section>

</main>
</body>
</html>
```